Business Card Design Project

Need a business card designed for a horse racing/gambling centered company.
Company name is BrightQuill.com.au
Company colours are similar to those in the logo.
Something clean and modern , designer given liberty to be creative.
Incorporate the logo is preferred.
Single or Double Sided fine
Must include :
Name
Mobile Number
Email Address
Reason: Apologies, I have been traveling unexpectedly with business and just need the extra two days to reply and give feedback before making a decision.
Industry/Entity Type
Business

```html
<!DOCTYPE html>
<html lang="en">
<head>
<meta charset="utf-8">
<title>BrightQuill.com.au – Business Card</title>
<link rel="stylesheet" href="https://fonts.googleapis.com/css2?family=Josefin+Sans:wght@400;700&display=swap">
<style>
  :root {
    --backdrop: #eeeae4;
    --teal: #1d9c98;
    --teal-deep: #17857f;
    --teal-light: #4fb9b5;
    --white: #ffffff;
    --strip-edge: #a9adae;
    --ink-teal: #1a8f8a;
    --card-shadow: rgba(0, 0, 0, 0.28);
  }
  * { box-sizing: border-box; margin: 0; padding: 0; }
  html, body {
    width: 1200px;
    height: 900px;
    overflow: hidden;
    background: var(--backdrop);
    font-family: "Josefin Sans", sans-serif;
  }
  .canvas {
    position: relative;
    width: 1200px;
    height: 900px;
  }
  .card {
    position: absolute;
    left: 290px;
    width: 593px;
    height: 361px;
    background: radial-gradient(ellipse 55% 60% at 50% 30%, var(--teal-light) 0%, var(--teal) 55%, var(--teal-deep) 100%);
    box-shadow: 0 6px 16px var(--card-shadow);
    overflow: hidden;
  }
  .card--front { top: 67px; }
  .card--back { top: 450px; }

  /* brand mark: plain circle with company name */
  .brand {
    position: absolute;
    display: flex;
    align-items: center;
    justify-content: center;
    border-radius: 50%;
    background: var(--white);
    box-shadow: 0 3px 8px rgba(0,0,0,0.25);
  }
  .brand__name {
    font-family: "Josefin Sans", sans-serif;
    font-weight: 700;
    color: var(--ink-teal);
    letter-spacing: 0.04em;
    text-transform: uppercase;
    text-align: center;
    line-height: 1.15;
  }
  .card--front .brand {
    left: 154px;
    top: 36px;
    width: 286px;
    height: 286px;
  }
  .card--front .brand__name { font-size: 26px; }

  .card--back .brand {
    left: 16px;
    top: 86px;
    width: 186px;
    height: 186px;
    z-index: 2;
  }
  .card--back .brand__name { font-size: 17px; }

  .contact-strip {
    position: absolute;
    left: 165px;
    top: 98px;
    width: 428px;
    height: 158px;
    background: var(--white);
    border: 4px solid var(--strip-edge);
    border-right: none;
    box-shadow: 0 4px 8px rgba(0,0,0,0.22);
  }
  .contact-list {
    position: absolute;
    right: 20px;
    top: 46px;
    list-style: none;
    text-align: right;
    color: var(--ink-teal);
    font-size: 15px;
    font-variant: small-caps;
    letter-spacing: 0.16em;
    line-height: 22px;
  }
</style>
</head>
<body>
<main class="canvas">
  <section class="card card--front" aria-label="Business card front">
    <div class="brand">
      <span class="brand__name">BrightQuill<br>.com.au</span>
    </div>
  </section>

  <section class="card card--back" aria-label="Business card back">
    <div class="brand">
      <span class="brand__name">BrightQuill<br>.com.au</span>
    </div>
    <div class="contact-strip">
      <ul class="contact-list">
        <li>Name: Mark Ellison</li>
        <li>Phone : 0412558093</li>
        <li>Email: Mark@brightquill.com.au</li>
      </ul>
    </div>
  </section>
</main>
</body>
</html>
```